Tavorly - Landing Page

Need a landing page for a journal app. The app is based on a retrospective board, where each journal entry is split into 3 sections: "What went well", "What Didn't Go Well" and "Things To Try".
The landing page should match the style of all modern web application landing pages. Think Brimo, Quenta, Vexadro. I've included screenshots of the app.
One feature that I want to highlight that is not ready yet, is an AI coach. It will offer insights based on the history of the user's journal entries
1 page

```html
<!DOCTYPE html>
<html lang="en">
<head>
<meta charset="UTF-8">
<title>Tavorly - Your Daily Journal For Thoughtful Retrospectives</title>
<link rel="stylesheet" href="https://fonts.googleapis.com/css2?family=Poppins:wght@300;400;500;600;700&family=Montserrat:wght@400;500;600;700&display=swap">
<style>
:root{
  --blue:#0c4fb3;
  --blue-deep:#083c94;
  --blue-bright:#1c6fe0;
  --blue-soft:#a9c8f0;
  --blue-pale:#e6eef9;
  --navy:#14233f;
  --ink:#111827;
  --muted:#5b6474;
  --line:#dfe5ee;
  --white:#ffffff;
  --page:#f7f9fc;
}
*{box-sizing:border-box;margin:0;padding:0}
html,body{width:1200px;height:4932px;overflow:hidden}
body{font-family:"Poppins",sans-serif;color:var(--ink);background:var(--white);position:relative}
a{color:inherit;text-decoration:none}

/* ---------- Header & hero ---------- */
.hero{position:absolute;left:0;top:0;width:1200px;height:930px;
  background:linear-gradient(160deg,#1257c4 0%,var(--blue) 45%,var(--blue-deep) 100%);color:var(--white)}
.nav{position:absolute;top:18px;left:130px;right:130px;height:48px;display:flex;align-items:center}
.brand{font-weight:700;font-size:36px;letter-spacing:-.5px}
.nav-links{display:flex;gap:30px;margin-left:auto;margin-right:40px;font-size:14px}
.nav-actions{display:flex;gap:16px}
.btn{display:inline-flex;align-items:center;justify-content:center;font-family:"Poppins",sans-serif;font-weight:500;border-radius:4px;font-size:14px}
.btn-outline-light{border:1.5px solid var(--white);color:var(--white);width:96px;height:34px}
.btn-light{background:var(--blue-pale);color:var(--blue);width:96px;height:34px}
.hero-kicker{position:absolute;top:132px;width:100%;text-align:center;font-size:26px;font-weight:500}
.hero-title{position:absolute;top:176px;width:100%;text-align:center;font-size:42px;font-weight:700;line-height:1.25}
.hero-cta{position:absolute;top:300px;left:510px;width:180px;height:42px;background:var(--blue-pale);color:var(--blue);font-size:15px}

/* ---------- App mock ---------- */
.mock{position:absolute;background:var(--white);border-radius:10px;box-shadow:0 14px 40px rgba(10,40,100,.18);display:flex;overflow:hidden;border:1px solid var(--line)}
.mock-rail{background:var(--navy);display:flex;flex-direction:column;align-items:center;gap:18px;padding-top:22px}
.mock-rail i{display:block;width:14px;height:14px;border-radius:3px;background:#8ea3c7}
.mock-rail i.dot{width:8px;height:8px;border-radius:50%;margin-top:auto}
.mock-menu{background:#d6e4f7;padding:14px 0}
.mock-menu .mm{font-size:11px;padding:6px 12px;color:var(--navy)}
.mock-menu .mm.on{background:var(--blue);color:var(--white);font-weight:500}
.mock-body{flex:1;display:flex;flex-direction:column;background:#fafbfd}
.mock-top{display:flex;align-items:center;gap:10px;padding:10px 16px;border-bottom:1px solid var(--line);background:var(--white)}
.mock-top .brand-mini{font-weight:700;color:var(--blue);font-size:20px}
.mock-top .search{margin-left:auto;width:140px;height:20px;border:1px solid var(--line);border-radius:4px}
.mock-top .user{display:flex;align-items:center;gap:6px;font-size:9px;color:var(--muted)}
.mock-top .av{width:18px;height:18px;border-radius:50%;background:#c3ccd9}
.mock-main{flex:1;display:flex}
.mock-sheet{flex:1;margin:14px;background:var(--white);border:1px solid var(--line);border-radius:6px;padding:14px 18px;position:relative;display:flex;flex-direction:column}
.sheet-head{display:flex;justify-content:space-between;align-items:flex-start}
.sheet-head b{font-size:13px;display:block}
.sheet-head small{font-size:10px;color:var(--muted)}
.sheet-head .tag{background:var(--blue-soft);width:54px;height:14px;border-radius:3px}
.entry{display:flex;align-items:center;gap:10px;border:1px solid var(--line);border-radius:6px;padding:10px;margin-top:12px;box-shadow:0 2px 6px rgba(0,0,0,.05)}
.entry .av{width:28px;height:28px;border-radius:50%;background:#b9c3d1;flex:none}
.entry p{font-size:12px;font-weight:500;line-height:1.35}
.composer{margin-top:auto;display:flex;align-items:center;gap:8px;border:1px solid var(--line);border-radius:6px;padding:8px 10px;font-size:10px;color:var(--muted)}
.composer span{flex:1}
.composer i{width:10px;height:10px;border-radius:2px;background:#9aa6b8;display:block}
.mock-tools{width:16%;border-left:1px solid var(--line);background:var(--white);padding:14px 10px;display:flex;flex-wrap:wrap;align-content:flex-start;gap:8px}
.mock-tools i{display:block;width:14px;height:12px;border-radius:2px;background:#c8d0dc}
.mock-tools i.wide{width:100%;height:18px;background:#eef2f7}

.mock.sm .mock-menu .mm{font-size:8px;padding:4px 8px}
.mock.sm .entry{padding:7px;margin-top:8px}
.mock.sm .entry .av{width:20px;height:20px}
.mock.sm .entry p{font-size:9px}
.mock.sm .sheet-head b{font-size:10px}
.mock.sm .sheet-head small{font-size:8px}
.mock.sm .composer{font-size:7px;padding:5px 8px}
.mock.sm .mock-top{padding:7px 10px}
.mock.sm .mock-top .av{width:14px;height:14px}
.mock.sm .mock-top .user{font-size:7px}
.mock.sm .mock-sheet{margin:10px;padding:10px 12px}
.mock.sm .mock-rail{gap:12px;padding-top:14px}
.mock.sm .mock-rail i{width:10px;height:10px}

/* ---------- How it works ---------- */
.works{position:absolute;left:0;top:930px;width:1200px;height:1850px;background:var(--white)}
.eyebrow{font-size:20px;text-align:center;color:var(--ink)}
.section-title{font-size:40px;font-weight:700;text-align:center;line-height:1.3}
.section-title em{font-style:normal;color:var(--blue-bright)}
.works .eyebrow{position:absolute;top:150px;width:100%}
.works .section-title{position:absolute;top:190px;width:100%}
.step{position:absolute;width:440px}
.step-icon{width:48px;height:48px;border-radius:8px;background:var(--blue);display:flex;align-items:center;justify-content:center}
.step h3{font-family:"Montserrat",sans-serif;font-size:40px;font-weight:500;margin:20px 0 14px}
.step p{font-size:15px;line-height:1.6;color:#2d3340;margin-bottom:14px}
.btn-primary{background:var(--blue);color:var(--white);height:44px;padding:0 22px;font-size:14px;margin-top:4px}
.connector{position:absolute;left:0;top:0;pointer-events:none}

/* ---------- Why ---------- */
.why{position:absolute;left:0;top:2780px;width:1200px;height:620px;background:linear-gradient(160deg,#1257c4,var(--blue-deep));color:var(--white)}
.why .eyebrow{position:absolute;top:88px;width:100%;color:var(--white)}
.why .section-title{position:absolute;top:126px;width:100%}
.features{position:absolute;top:240px;left:140px;display:flex;gap:36px}
.feature{width:280px;height:200px;background:var(--white);color:var(--ink);border-radius:8px;padding:22px 24px;position:relative}
.feature h4{font-size:20px;font-weight:500;margin:14px 0 8px}
.feature p{font-size:11px;color:var(--muted);line-height:1.5;width:190px}
.feature .go{position:absolute;right:18px;bottom:18px;width:36px;height:36px;border-radius:50%;background:var(--blue-pale);display:flex;align-items:center;justify-content:center}
.why-actions{position:absolute;top:468px;left:0;width:100%;display:flex;justify-content:center;gap:24px}
.btn-pale{background:var(--blue-pale);color:var(--blue);width:120px;height:42px;font-size:12px}
.btn-ghost{border:1.5px solid var(--white);color:var(--white);width:120px;height:42px;font-size:12px}

/* ---------- Testimonials ---------- */
.testimonials{position:absolute;left:0;top:3400px;width:1200px;height:800px;background:var(--white)}
.testimonials .eyebrow{position:absolute;top:40px;width:100%}
.testimonials .section-title{position:absolute;top:80px;width:100%}
.quote-card{position:absolute;top:240px;left:88px;width:972px;height:460px;background:#edf2f8;border-radius:6px;overflow:hidden}
.stars{position:absolute;left:68px;top:92px}
.quote-text{position:absolute;left:68px;top:132px;width:530px;font-size:20px;line-height:32px;color:var(--ink)}
.quote-name{position:absolute;left:40px;top:372px}
.quote-name b{font-family:"Montserrat",sans-serif;font-size:16px;font-weight:700;display:block}
.quote-name small{display:block;font-size:11px;color:var(--muted);margin-left:40px;margin-top:2px}
.quote-photo{position:absolute;right:0;top:0;width:350px;height:460px;background:linear-gradient(180deg,#c9ccd0 0%,#a9a49d 55%,#3f3b39 100%)}
.quote-next{position:absolute;top:240px;left:1150px;width:120px;height:460px;background:#edf2f8;border-radius:6px;padding:96px 20px}
.slider-btn{position:absolute;left:1092px;width:40px;height:40px;border-radius:50%;background:var(--blue-pale);display:flex;align-items:center;justify-content:center}

/* ---------- CTA ---------- */
.cta{position:absolute;left:0;top:4200px;width:1200px;height:360px;background:linear-gradient(160deg,#1257c4,var(--blue-deep));color:var(--white)}
.cta .eyebrow{position:absolute;top:84px;width:100%;color:var(--white)}
.cta .section-title{position:absolute;top:122px;width:100%}
.cta .btn{position:absolute;top:236px;left:540px;width:120px;height:42px;background:var(--blue-pale);color:var(--blue);font-size:13px}

/* ---------- Footer ---------- */
.footer{position:absolute;left:0;top:4560px;width:1200px;height:372px;background:var(--page)}
.footer .brand{position:absolute;left:230px;top:66px;color:var(--blue);font-size:40px}
.social{position:absolute;left:258px;top:136px;display:flex;gap:14px}
.social span{width:28px;height:28px;border-radius:50%;background:#e3e8ef}
.foot-col{position:absolute;top:70px}
.foot-col h5{font-size:12px;font-weight:600;margin-bottom:4px}
.foot-col .rule{width:40px;height:2px;background:var(--blue);margin-bottom:12px}
.foot-col li{list-style:none;font-size:11px;color:var(--muted);margin-bottom:8px}
.contact-row{display:flex;gap:10px;align-items:flex-start;font-size:11px;color:var(--muted);margin-bottom:16px;line-height:1.45}
.contact-row b{color:var(--ink);font-weight:500}
.copyright{position:absolute;bottom:24px;width:100%;text-align:center;font-size:10px;color:var(--muted);border-top:1px solid var(--line);padding-top:14px}
.to-top{position:absolute;right:22px;bottom:20px;width:36px;height:36px;background:var(--blue);border-radius:4px;display:flex;align-items:center;justify-content:center}
</style>
</head>
<body>

<header class="hero">
  <nav class="nav">
    <div class="brand">Tavorly</div>
    <div class="nav-links"><a>Home</a><a>About</a><a>Features</a><a>How it Works</a><a>Contact</a></div>
    <div class="nav-actions"><a class="btn btn-outline-light">Login</a><a class="btn btn-light">Sign Up</a></div>
  </nav>
  <p class="hero-kicker">Reflect, Grow, Succeed.</p>
  <h1 class="hero-title">Your Daily Journal For Thoughtful<br>Retrospectives.</h1>
  <a class="btn hero-cta">Start Your Journey</a>
</header>

<div class="mock" style="left:140px;top:400px;width:920px;height:572px">
  <div class="mock-rail" style="width:42px"><i></i><i></i><i></i><i></i><i class="dot"></i><i class="dot" style="margin-top:0"></i><i class="dot" style="margin-top:0;margin-bottom:30px"></i></div>
  <div class="mock-menu" style="width:104px">
    <div class="mm on">What Went Well</div><div class="mm">What Didn't Go</div><div class="mm">Things To Try</div>
  </div>
  <div class="mock-body">
    <div class="mock-top"><span class="brand-mini" style="font-size:26px">Tavorly</span><span class="search"></span><span class="user"><span class="av"></span>Darin Colwell</span></div>
    <div class="mock-main">
      <div class="mock-sheet" style="margin:18px 24px">
        <div class="sheet-head"><div><b>Entry</b><small>Thu Aug 8 2024</small></div><span class="tag"></span></div>
        <div class="entry" style="width:300px;margin-top:22px"><span class="av"></span><p>Completed all scheduled workouts this week</p></div>
        <div class="entry" style="width:300px"><span class="av"></span><p>Increased bench press weight by 10 pounds.</p></div>
        <div class="composer"><span>Maintained consistent energy levels throughout sessions</span><i></i><i></i></div>
      </div>
      <div class="mock-tools"><i class="wide"></i><i></i><i></i><i></i><i></i><i></i><i></i><i></i><i></i></div>
    </div>
  </div>
</div>

<section class="works">
  <p class="eyebrow">How Tavorly Works</p>
  <h2 class="section-title">The Tavorly Method Simple<br>Steps to <em>Growth</em></h2>

  <svg class="connector" width="1200" height="1850" viewBox="0 0 1200 1850" aria-hidden="true">
    <path d="M660 660 C660 760 660 780 660 820" fill="none" stroke="#9aa6b8" stroke-width="2" stroke-dasharray="6 6"/>
    <path d="M300 1200 C300 1300 300 1340 300 1370" fill="none" stroke="#9aa6b8" stroke-width="2" stroke-dasharray="6 6"/>
    <path d="M660 1120 C660 1230 600 1300 560 1370" fill="none" stroke="#9aa6b8" stroke-width="2" stroke-dasharray="6 6"/>
  </svg>

  <article class="step" style="left:140px;top:320px">
    <div class="step-icon"><svg width="24" height="24" viewBox="0 0 24 24"><path d="M3 11h4v10H3zM9 21V11l4-8c1.5 0 2.5 1 2.2 2.6L14.5 9H20c1 0 1.8 1 1.5 2l-2 8c-.3 1-1 2-2 2z" fill="#fff"/></svg></div>
    <h3>What Went Well</h3>
    <p>It is a long established fact that a reader will be distracted by the readable content of a page when looking at its layout. The point of using Lorem Ipsum is that it has a more-or-less normal distribution of letters, as opposed to using 'Content here.</p>
    <p>Lorem Ipsum is simply dummy text of the printing and typesetting industry. Lorem Ipsum has been the industry's standard dummy text ever since the 1500s</p>
    <a class="btn btn-primary">Try Tavorly Now</a>
  </article>
  <div class="mock sm" style="left:668px;top:318px;width:540px;height:332px">
    <div class="mock-rail" style="width:30px"><i></i><i></i><i></i><i></i></div>
    <div class="mock-body">
      <div class="mock-top"><span class="user" style="margin-left:auto"><span class="av"></span>Darin Colwell</span></div>
      <div class="mock-main">
        <div class="mock-sheet">
          <div class="sheet-head"><div><b>Entry</b><small>Thu Aug 8 2024</small></div><span class="tag"></span></div>
          <div class="entry" style="width:230px"><span class="av"></span><p>Completed all scheduled workouts this week</p></div>
          <div class="entry" style="width:230px"><span class="av"></span><p>Increased bench press weight by 10 pounds.</p></div>
          <div class="composer"><span>Maintained steady energy levels</span><i></i></div>
        </div>
        <div class="mock-tools"><i class="wide"></i><i></i><i></i><i></i><i></i></div>
      </div>
    </div>
  </div>

  <article class="step" style="left:640px;top:820px">
    <div class="step-icon"><svg width="24" height="24" viewBox="0 0 24 24"><path d="M12 3 2 21h20z" fill="#fff"/><path d="M12 10v5M12 17v1.5" stroke="#0c4fb3" stroke-width="2"/></svg></div>
    <h3>What Didn't Go Well?</h3>
    <p>It is a long established fact that a reader will be distracted by the readable content of a page when looking at its layout. The point of using Lorem Ipsum is that it has a more-or-less normal distribution of letters, as opposed to using 'Content here.</p>
    <p>Lorem Ipsum is simply dummy text of the printing and typesetting industry. Lorem Ipsum has been the industry's standard dummy text ever since the 1500s</p>
    <a class="btn btn-primary">Try Tavorly Now</a>
  </article>
  <div class="mock sm" style="left:-8px;top:858px;width:568px;height:332px">
    <div class="mock-body">
      <div class="mock-top"><span class="user"><span class="av"></span>Darin Colwell</span></div>
      <div class="mock-main">
        <div class="mock-sheet">
          <div class="sheet-head"><div><b>Entry</b><small>Thu Aug 8 2024</small></div><span class="tag"></span></div>
          <div class="entry" style="width:250px"><span class="av"></span><p>Struggled with form on deadlifts, leading to lower back discomfort</p></div>
          <div class="entry" style="width:250px"><span class="av"></span><p>Skipped cool-down, leading to increased muscle soreness.</p></div>
          <div class="composer"><span>Felt tired during late sessions</span><i></i></div>
        </div>
        <div class="mock-tools" style="width:14%"><i class="wide"></i><i></i><i></i><i></i></div>
      </div>
    </div>
  </div>

  <article class="step" style="left:140px;top:1370px">
    <div class="step-icon"><svg width="24" height="24" viewBox="0 0 24 24"><circle cx="12" cy="6" r="3" fill="#fff"/><path d="M6 21v-6c0-3 2.5-5 6-5s6 2 6 5v6z" fill="#fff"/></svg></div>
    <h3>Things To Try</h3>
    <p>It is a long established fact that a reader will be distracted by the readable content of a page when looking at its layout. The point of using Lorem Ipsum is that it has a more-or-less normal distribution of letters, as opposed to using 'Content here.</p>
    <p>Lorem Ipsum is simply dummy text of the printing and typesetting industry. Lorem Ipsum has been the industry's standard dummy text ever since the 1500s</p>
    <a class="btn btn-primary">Try Tavorly Now</a>
  </article>
  <div class="mock sm" style="left:668px;top:1470px;width:540px;height:320px">
    <div class="mock-rail" style="width:30px"><i></i><i></i><i></i><i></i></div>
    <div class="mock-body">
      <div class="mock-top"><span class="user" style="margin-left:auto"><span class="av"></span>Darin Colwell</span></div>
      <div class="mock-main">
        <div class="mock-sheet">
          <div class="sheet-head"><div><b>Entry</b><small>Thu Aug 8 2024</small></div><span class="tag"></span></div>
          <div class="entry" style="width:240px"><span class="av"></span><p>Focus on flexibility training this week and mobility drills.</p></div>
          <div class="entry" style="width:240px"><span class="av"></span><p>Set reminders for post-workout stretching to prevent soreness.</p></div>
          <div class="composer"><span>Plan rest days in advance</span><i></i></div>
        </div>
        <div class="mock-tools"><i class="wide"></i><i></i><i></i><i></i></div>
      </div>
    </div>
  </div>
</section>

<section class="why">
  <p class="eyebrow">Why Tavorly?</p>
  <h2 class="section-title">Discover the Power of<br>Tavorly</h2>
  <div class="features">
    <div class="feature">
      <svg width="40" height="40" viewBox="0 0 40 40"><circle cx="20" cy="17" r="12" fill="#0c4fb3"/><rect x="15" y="28" width="10" height="6" rx="1" fill="#0c4fb3"/></svg>
      <h4>Mental Clarity</h4><p>Regular reflection helps clear your mind and stay focused.</p>
      <span class="go"><svg width="14" height="14" viewBox="0 0 14 14"><path d="M3 11 11 3M5 3h6v6" stroke="#0c4fb3" stroke-width="1.8" fill="none"/></svg></span>
    </div>
    <div class="feature">
      <svg width="48" height="40" viewBox="0 0 48 40"><circle cx="10" cy="22" r="5" fill="#0c4fb3"/><circle cx="24" cy="18" r="5" fill="#0c4fb3"/><circle cx="38" cy="22" r="5" fill="#0c4fb3"/><path d="M8 12 22 4l6 5 12-7" stroke="#0c4fb3" stroke-width="2.5" fill="none"/></svg>
      <h4>Personal Growth</h4><p>Track your progress and improve over time.</p>
      <span class="go"><svg width="14" height="14" viewBox="0 0 14 14"><path d="M3 11 11 3M5 3h6v6" stroke="#0c4fb3" stroke-width="1.8" fill="none"/></svg></span>
    </div>
    <div class="feature">
      <svg width="40" height="40" viewBox="0 0 40 40"><path d="M16 6v18l-4-3-3 3 9 12h14l3-14-12-3V6a3 3 0 0 0-7 0z" fill="#0c4fb3"/></svg>
      <h4>Ease of Use</h4><p>Simple intuitive design for seamless journaling.</p>
      <span class="go"><svg width="14" height="14" viewBox="0 0 14 14"><path d="M3 11 11 3M5 3h6v6" stroke="#0c4fb3" stroke-width="1.8" fill="none"/></svg></span>
    </div>
  </div>
  <div class="why-actions"><a class="btn btn-pale">Get Started</a><a class="btn btn-ghost">Learn More</a></div>
</section>

<section class="testimonials">
  <p class="eyebrow">Hear from Our Users</p>
  <h2 class="section-title">Testimonials From Our<br><em>Clients.</em></h2>
  <div class="quote-card">
    <svg class="stars" width="110" height="20" viewBox="0 0 110 20" aria-label="Five stars"><g fill="#0c4fb3"><path id="st" d="M10 1l2.7 6 6.3.5-4.8 4.2 1.5 6.3L10 14.6 4.3 18l1.5-6.3L1 7.5 7.3 7z"/><use href="#st" x="22"/><use href="#st" x="44"/><use href="#st" x="66"/><use href="#st" x="88"/></g></svg>
    <blockquote class="quote-text">Working with Norvane Labs has been transformative for our business. Their expertise in technological consulting, particularly in digital automation, AI, and Big Data, has streamlined our operations and significantly boosted our efficiency.</blockquote>
    <div class="quote-name"><b>-DARIN COLWELL</b><small>Co-CEO, Pellrow</small></div>
    <div class="quote-photo" role="img" aria-label="Portrait photo of the client giving the testimonial"></div>
  </div>
  <div class="quote-next"><svg width="60" height="16" viewBox="0 0 60 16"><g fill="#0c4fb3"><circle cx="6" cy="8" r="5"/><circle cx="20" cy="8" r="5"/></g></svg></div>
  <span class="slider-btn" style="top:330px"><svg width="14" height="14" viewBox="0 0 14 14"><path d="M11 3 3 11M3 5v6h6" stroke="#0c4fb3" stroke-width="1.8" fill="none"/></svg></span>
  <span class="slider-btn" style="top:480px;background:var(--blue)"><svg width="14" height="14" viewBox="0 0 14 14"><path d="M3 11 11 3M5 3h6v6" stroke="#fff" stroke-width="1.8" fill="none"/></svg></span>
</section>

<section class="cta">
  <p class="eyebrow">Ready to Start Reflecting?</p>
  <h2 class="section-title">Join A Community Of Mindful<br>Individuals.</h2>
  <a class="btn">Contact Us</a>
</section>

<footer class="footer">
  <div class="brand">Tavorly</div>
  <div class="social"><span></span><span></span><span></span></div>
  <div class="foot-col" style="left:530px">
    <h5>QUICK LINKS</h5><div class="rule"></div>
    <ul><li>Home</li><li>About</li><li>Features</li><li>How It Works</li><li>Contact</li></ul>
  </div>
  <div class="foot-col" style="left:756px">
    <h5>CONTACT US</h5><div class="rule"></div>
    <div class="contact-row"><svg width="14" height="14" viewBox="0 0 14 14"><path d="M7 1a4 4 0 0 1 4 4c0 3-4 8-4 8S3 8 3 5a4 4 0 0 1 4-4z" fill="#0c4fb3"/></svg><span>210 Harbor Lane, Suite 4<br>Fairmont City, 20418</span></div>
    <div class="contact-row"><svg width="14" height="14" viewBox="0 0 14 14"><path d="M3 1h3l1 3-2 1c1 2 2 3 4 4l1-2 3 1v3c0 1-1 2-2 2C6 13 1 8 1 3c0-1 1-2 2-2z" fill="#0c4fb3"/></svg><span>Call us : <b>+1 (555) 0142 776</b></span></div>
    <div class="contact-row"><svg width="14" height="14" viewBox="0 0 14 14"><rect x="1" y="3" width="12" height="8" rx="1" fill="#0c4fb3"/><path d="M1 4l6 4 6-4" stroke="#fff" fill="none"/></svg><span>Email :<br>info@tavorly.com</span></div>
  </div>
  <p class="copyright">Copyright © 2024 Tavorly. All Rights Reserved.</p>
  <span class="to-top"><svg width="14" height="14" viewBox="0 0 14 14"><path d="M7 12V2M3 6l4-4 4 4" stroke="#fff" stroke-width="2" fill="none"/></svg></span>
</footer>

</body>
</html>
```